Business Card and Letterhead for Nurlo - modern real estate business

I need a double sided business card design for Nurlo. Please see business card brief here https://papers.trelvimo.net/sheet/q/7XrTbaLeZpMmQ2uWvd9HkCj4yNoEfsGi3lRtAz_pk/view?mode=shared

Please feel free to design the business cards however you feel best. I am happy to give some creative freedoms and then provide feedback from there.

Please then also create a letterhead to match the business card design

Colors

Designer to choose colors to be used in the design.

Requirements
Must have
• Must be a modern, elegant business card which looks very professional

```html
<!DOCTYPE html>
<html lang="en">
<head>
<meta charset="utf-8">
<title>Nurlo Business Card</title>
<link rel="stylesheet" href="https://fonts.googleapis.com/css2?family=Montserrat:wght@400;500;600&display=swap">
<style>
  :root {
    --bg: #dcdde0;
    --ink: #231f20;
    --red: #e3151c;
    --white: #ffffff;
    --paper: #f9f9f9;
    --text: #1e1e1e;
  }
  * { margin: 0; padding: 0; box-sizing: border-box; }
  html, body { width: 1200px; height: 800px; overflow: hidden; }
  body {
    background: var(--bg);
    font-family: "Montserrat", sans-serif;
    position: relative;
  }
  .card {
    position: absolute;
    width: 540px;
    height: 309px;
    top: 245px;
    overflow: hidden;
    box-shadow: 0 6px 18px rgba(0,0,0,0.18);
  }
  .card--back { left: 40px; background: var(--paper); }
  .card--front {
    left: 620px;
    background: var(--ink);
    display: flex;
    align-items: center;
    justify-content: center;
  }
  .brand-name {
    font-family: "Montserrat", sans-serif;
    font-weight: 600;
    color: var(--red);
    letter-spacing: 0.06em;
    line-height: 1;
  }
  .card--front .brand-name { font-size: 72px; }
  .card--back .brand-name {
    position: absolute;
    left: 38px;
    top: 40px;
    font-size: 50px;
  }
  .name-band {
    position: absolute;
    left: 0;
    top: 120px;
    width: 340px;
    height: 56px;
    background: var(--ink);
    padding: 10px 0 0 38px;
  }
  .agent-name {
    color: var(--red);
    font-weight: 500;
    font-size: 15px;
    letter-spacing: 0.03em;
    text-transform: uppercase;
  }
  .agent-title {
    color: var(--white);
    font-size: 12.5px;
    margin-top: 2px;
    letter-spacing: 0.02em;
  }
  .address {
    position: absolute;
    left: 38px;
    top: 190px;
    font-size: 12.5px;
    line-height: 1.35;
    color: var(--text);
  }
  .contact-list {
    position: absolute;
    left: 38px;
    top: 230px;
    list-style: none;
    font-size: 12.5px;
    color: var(--text);
  }
  .contact-list li { display: flex; align-items: center; gap: 6px; line-height: 1.4; }
  .contact-list svg { width: 11px; height: 11px; flex: none; }
  .accent-bar {
    position: absolute;
    left: 400px;
    top: 170px;
    width: 140px;
    height: 42px;
    background: var(--red);
  }
  .photo-ring {
    position: absolute;
    left: 318px;
    top: 98px;
    width: 162px;
    height: 162px;
    border-radius: 50%;
    background: var(--white);
    border: 3px solid var(--red);
    padding: 6px;
  }
  .photo {
    width: 100%;
    height: 100%;
    border-radius: 50%;
    background: radial-gradient(circle at 50% 40%, #b9a89a 0%, #8a8f78 45%, #3a3d3a 80%, #262626 100%);
  }
</style>
</head>
<body>
  <section class="card card--back" aria-label="Business card, contact side">
    <div class="brand-name">NURLO</div>
    <div class="name-band">
      <p class="agent-name">Dane Whitfield</p>
      <p class="agent-title">Licenced Real Estate Agent</p>
    </div>
    <p class="address">PO Box 3174<br>Brenvale NSW 2791</p>
    <ul class="contact-list">
      <li>
        <svg viewBox="0 0 24 24" aria-hidden="true"><path fill="#e3151c" d="M6.6 10.8a15.1 15.1 0 0 0 6.6 6.6l2.2-2.2c.3-.3.7-.4 1-.2 1.1.4 2.3.6 3.6.6.6 0 1 .4 1 1V20c0 .6-.4 1-1 1C10.6 21 3 13.4 3 4c0-.6.4-1 1-1h3.5c.6 0 1 .4 1 1 0 1.3.2 2.5.6 3.6.1.3 0 .7-.2 1z"/></svg>
        0412 555 019
      </li>
      <li>
        <svg viewBox="0 0 24 24" aria-hidden="true"><rect x="2" y="5" width="20" height="14" fill="none" stroke="#e3151c" stroke-width="2.5"/><path d="M2 5l10 8 10-8" fill="none" stroke="#e3151c" stroke-width="2.5"/></svg>
        dane@nurlo.com
      </li>
      <li>
        <svg viewBox="0 0 24 24" aria-hidden="true"><circle cx="12" cy="12" r="10" fill="none" stroke="#e3151c" stroke-width="2.5"/><path d="M2 12h20M12 2c3 3 3 17 0 20M12 2c-3 3-3 17 0 20" fill="none" stroke="#e3151c" stroke-width="2"/></svg>
        www.nurlo.com
      </li>
    </ul>
    <div class="accent-bar"></div>
    <div class="photo-ring">
      <div class="photo" role="img" aria-label="Portrait photo of the agent in a dark shirt, outdoor background"></div>
    </div>
  </section>

  <section class="card card--front" aria-label="Business card, brand side">
    <div class="brand-name">NURLO</div>
  </section>
</body>
</html>
```